New baby product company needs product trifold

We are a new company with products based from 30+ years of nursing experience with babies. Most of our products are made from 100% organic materials. We need a product brochure to place in waiting rooms of Labor and delivery doctors and birthing centers. The front page needs to grab their attention and invite them to pick it up and read more. Target audience expecting and new mothers ages 22-39. The final design should communicate our expertise and experience of knowing what a baby needs.
Need extra days to review
Baby

```html
<!DOCTYPE html>
<html lang="en">
<head>
<meta charset="utf-8">
<title>Nestling Baby Products – Product Trifold</title>
<link href="https://fonts.googleapis.com/css2?family=Fjalla+One&family=Roboto+Condensed:wght@700&display=swap" rel="stylesheet">
<style>
  :root{
    --stage:#dcdcdc;
    --sky:#bde2ee;
    --sky-shadow:#9fcbdc;
    --paper:#ffffff;
    --ring:#a9d6e6;
    --coral:#e9676a;
    --heart:#ec7f81;
    --ink-blue:#1d6fc1;
    --brand-green:#3f9a4a;
    --skin-light:#f6d9c4;
    --skin-mid:#e9b89a;
  }
  *{box-sizing:border-box;margin:0;padding:0}
  html,body{width:1200px;height:800px;overflow:hidden;background:var(--stage)}
  .trifold{
    position:absolute;left:40px;top:40px;width:1120px;height:720px;
    background:var(--sky);overflow:hidden;
    box-shadow:0 8px 24px rgba(0,0,0,.18);
  }
  .shapes{position:absolute;inset:0}
  .copy{position:absolute}
  .product-title{
    font-family:"Fjalla One",sans-serif;color:var(--coral);
    font-size:34px;line-height:1.05;font-weight:400;
  }
  .product-text{
    font-family:"Roboto Condensed",sans-serif;font-weight:700;
    color:var(--ink-blue);font-size:18px;line-height:1.3;
  }
  .calm-sachet{left:170px;top:150px;width:320px;text-align:center}
  .calm-sachet .product-text{margin-top:10px}
  .snug-pod{left:560px;top:110px;width:250px;text-align:center}
  .snug-pod .product-title{text-align:left}
  .snug-pod .product-text{margin-top:14px}
  .bath-hug-title{left:735px;top:405px;width:150px;text-align:left}
  .bath-hug-text{left:725px;top:525px;width:320px;text-align:center}
  .photo{position:absolute}
  .baby-photo{
    left:40px;top:420px;width:440px;height:300px;
    border-radius:220px 200px 0 0;
    background:radial-gradient(ellipse at 45% 55%,var(--skin-light) 0%,var(--skin-mid) 70%,rgba(233,184,154,0) 100%);
  }
  .product-shot{
    border-radius:14px;
    background:linear-gradient(160deg,#ffffff 0%,#e9eef2 60%,#cfd8df 100%);
    box-shadow:0 3px 8px rgba(0,0,0,.15);
  }
  .shot-calm-sachet{left:470px;top:405px;width:90px;height:100px;transform:rotate(-8deg)}
  .shot-snug-pod{left:835px;top:160px;width:95px;height:140px}
  .shot-bath-hug{left:885px;top:335px;width:100px;height:110px}
  .brand{
    position:absolute;left:495px;top:595px;display:flex;align-items:center;gap:10px;
  }
  .brand-dot{width:56px;height:56px;border-radius:50%;background:var(--brand-green)}
  .brand-name{
    font-family:"Roboto Condensed",sans-serif;font-weight:700;
    color:var(--ink-blue);font-size:34px;line-height:1;
  }
  .brand-name small{display:block;font-size:16px;font-weight:700;margin-top:2px}
</style>
</head>
<body>
<main class="trifold">
  <svg class="shapes" width="1120" height="720" viewBox="0 0 1120 720">
    <defs>
      <symbol id="scallop" viewBox="-100 -100 200 200">
        <path d="M90 0 A19 19 0 0 1 83.15 34.44 A19 19 0 0 1 63.64 63.64 A19 19 0 0 1 34.44 83.15 A19 19 0 0 1 0 90 A19 19 0 0 1 -34.44 83.15 A19 19 0 0 1 -63.64 63.64 A19 19 0 0 1 -83.15 34.44 A19 19 0 0 1 -90 0 A19 19 0 0 1 -83.15 -34.44 A19 19 0 0 1 -63.64 -63.64 A19 19 0 0 1 -34.44 -83.15 A19 19 0 0 1 0 -90 A19 19 0 0 1 34.44 -83.15 A19 19 0 0 1 63.64 -63.64 A19 19 0 0 1 83.15 -34.44 A19 19 0 0 1 90 0Z"/>
      </symbol>
      <symbol id="heart" viewBox="0 0 100 90">
        <path d="M50 88 C20 65 0 48 0 26 C0 10 12 0 27 0 C38 0 46 6 50 15 C54 6 62 0 73 0 C88 0 100 10 100 26 C100 48 80 65 50 88Z"/>
      </symbol>
    </defs>

    <g class="scallop-calm-sachet">
      <use href="#scallop" x="118" y="38" width="440" height="440" fill="var(--sky-shadow)"/>
      <use href="#scallop" x="110" y="28" width="440" height="440" fill="var(--paper)"/>
      <circle cx="330" cy="248" r="172" fill="none" stroke="var(--ring)" stroke-width="3" stroke-dasharray="2 8" stroke-linecap="round"/>
    </g>
    <g class="scallop-snug-pod">
      <use href="#scallop" x="508" y="10" width="440" height="440" fill="var(--sky-shadow)"/>
      <use href="#scallop" x="500" y="0" width="440" height="440" fill="var(--paper)"/>
      <circle cx="720" cy="220" r="172" fill="none" stroke="var(--ring)" stroke-width="3" stroke-dasharray="2 8" stroke-linecap="round"/>
    </g>
    <g class="scallop-bath-hug">
      <use href="#scallop" x="668" y="290" width="440" height="440" fill="var(--sky-shadow)"/>
      <use href="#scallop" x="660" y="280" width="440" height="440" fill="var(--paper)"/>
      <circle cx="880" cy="500" r="172" fill="none" stroke="var(--ring)" stroke-width="3" stroke-dasharray="2 8" stroke-linecap="round"/>
    </g>

    <use class="heart-mark" href="#heart" x="445" y="415" width="120" height="108" fill="var(--heart)"/>
    <use class="heart-mark" href="#heart" x="805" y="175" width="160" height="144" fill="var(--heart)"/>
    <use class="heart-mark" href="#heart" x="900" y="335" width="140" height="126" fill="var(--heart)"/>
  </svg>

  <div class="photo baby-photo" role="img" aria-label="Photo of a smiling baby in a diaper sitting and reaching up toward the product"></div>

  <div class="photo product-shot shot-calm-sachet" role="img" aria-label="Photo of the Calm Sachet with a white ribbon and tag"></div>
  <div class="photo product-shot shot-snug-pod" role="img" aria-label="Photo of the Snug Pod in its white cotton drawstring bag"></div>
  <div class="photo product-shot shot-bath-hug" role="img" aria-label="Photo of the Bath Hug in its white cotton drawstring bag"></div>

  <section class="copy calm-sachet">
    <h2 class="product-title">Nestling Calm Sachet</h2>
    <p class="product-text">Turns bath time into a soothing moment for you and your little one. A gentler, calmer way to wash your baby.</p>
  </section>

  <section class="copy snug-pod">
    <h2 class="product-title">Nestling Snug Pod</h2>
    <p class="product-text">Gentle support for your baby at nap time - offering a warm, safe and snuggly space. Sewn from 100% organic soft cotton for peace of mind.</p>
  </section>

  <h2 class="copy product-title bath-hug-title">Nestling Bath Hug</h2>
  <p class="copy product-text bath-hug-text">Keeps your baby warm and calm from tub to towel. A softer, more peaceful way to end every bath.</p>

  <div class="brand">
    <span class="brand-dot"></span>
    <p class="brand-name">Nestling<small>baby products</small></p>
  </div>
</main>
</body>
</html>
```